Business Card Design for Small Electrical Contractor

I need to update my business card into something a little more modern. We are a small electrical contracting company. We service domestic and commercial places around Sydney. We have 2 logo designs at the moment. I have uploaded both and 2 different sizes to work with.

Industry/Entity Type

Business

Contact Information for Business Card

Leo Hartigan
8/21-23 Birch Rd, Kelsworth 2087
t - (02) 9381 4720
m - 0427 815 903
E - info@hartiganelx.com.au
W - hartiganelx.com.au
ABN: 42 907 551 316

Font styles to use
Sans Serif

Requirements
Must have
• I would also like to see the below fit on somewhere aswell
• - Licensed Electrician
• - Level 2 (Cat 1 & 4)
• - Domestic
• - Commercial
• - Repairs and Installations
• - Data
Nice to have
• Try and keep similar colours as logo
Should not have
• No lightning bolts or light globes. Smart and professional please.

```html
<!DOCTYPE html>
<html lang="en">
<head>
<meta charset="utf-8">
<title>Hartigan Electrical – Business Card</title>
<link href="https://fonts.googleapis.com/css2?family=Arimo:wght@400;700&display=swap" rel="stylesheet">
<style>
  :root{
    --bg:#e9e6e1;
    --card:#ffffff;
    --orange:#ec8a24;
    --teal:#1f3d38;
    --ink:#3d3d3d;
    --shadow:rgba(0,0,0,.14);
  }
  *{box-sizing:border-box;margin:0;padding:0}
  html,body{width:1200px;height:843px;overflow:hidden}
  body{
    background:var(--bg);
    font-family:"Arimo",Arial,sans-serif;
    color:var(--ink);
    display:flex;align-items:center;justify-content:center;gap:60px;
  }
  .card{
    position:relative;
    width:525px;height:300px;
    background:var(--card);
    box-shadow:0 3px 10px var(--shadow);
  }
  /* Front */
  .brand{
    position:absolute;right:40px;top:40px;
    text-align:right;
  }
  .brand-name{
    display:flex;align-items:center;justify-content:flex-end;gap:10px;
    font-size:30px;font-weight:700;color:var(--teal);letter-spacing:.5px;
  }
  .brand-dot{width:14px;height:14px;border-radius:50%;background:var(--orange)}
  .brand-rule{height:2px;background:var(--orange);margin:8px 0 6px auto;width:250px}
  .abn{font-size:12px;color:var(--ink);letter-spacing:.5px}
  .abn b{color:var(--orange)}
  .services{
    position:absolute;left:40px;bottom:38px;
    list-style:none;font-size:15px;line-height:24px;color:var(--ink);
  }
  .services li::before{content:"•";margin-right:8px}
  .services .sep{margin:0 8px}
  /* Back */
  .person{
    position:absolute;left:48px;top:42px;
    font-size:22px;font-weight:700;color:var(--orange);letter-spacing:.5px;
  }
  .person-rule{
    position:absolute;left:48px;top:78px;width:95px;height:2px;background:var(--teal);
  }
  .contacts{
    position:absolute;left:48px;top:98px;list-style:none;font-size:15px;line-height:22px;
  }
  .contacts li{display:flex;align-items:flex-start;gap:12px}
  .contacts svg{width:16px;height:16px;flex:none;margin-top:3px;fill:var(--orange)}
  .contacts .addr{margin-bottom:4px}
</style>
</head>
<body>

<section class="card card-front">
  <div class="brand">
    <div class="brand-name"><span class="brand-dot"></span>Hartigan Electrical</div>
    <div class="brand-rule"></div>
    <div class="abn"><b>ABN:</b> 42 907 551 316</div>
  </div>
  <ul class="services">
    <li>Licensed Electrician</li>
    <li>Level 2 (Cat 1 &amp; 4)</li>
    <li>Domestic<span class="sep">•</span>Commercial</li>
    <li>Repairs and Installations<span class="sep">•</span>Data</li>
  </ul>
</section>

<section class="card card-back">
  <h1 class="person">LEO HARTIGAN</h1>
  <div class="person-rule"></div>
  <ul class="contacts">
    <li class="addr">
      <svg viewBox="0 0 16 16"><path d="M8 0a5.5 5.5 0 0 0-5.5 5.5C2.5 10 8 16 8 16s5.5-6 5.5-10.5A5.5 5.5 0 0 0 8 0zm0 8a2.5 2.5 0 1 1 0-5 2.5 2.5 0 0 1 0 5z"/></svg>
      <span>8/21-23 Birch Rd<br>Kelsworth 2087</span>
    </li>
    <li>
      <svg viewBox="0 0 16 16"><path d="M1 5c0-2 3-3 7-3s7 1 7 3v1h-4V4.5H5V6H1zM3 7h10l1 7H2z"/></svg>
      <span>(02) 9381 4720</span>
    </li>
    <li>
      <svg viewBox="0 0 16 16"><path d="M4.5 0h7A1.5 1.5 0 0 1 13 1.5v13a1.5 1.5 0 0 1-1.5 1.5h-7A1.5 1.5 0 0 1 3 14.5v-13A1.5 1.5 0 0 1 4.5 0zM5 2v10h6V2zm3 11a1 1 0 1 0 0 2 1 1 0 0 0 0-2z"/></svg>
      <span>0427 815 903</span>
    </li>
    <li>
      <svg viewBox="0 0 16 16"><path d="M1 3h14v10H1zm1.5 1.5L8 9l5.5-4.5z"/></svg>
      <span>info@hartiganelx.com.au</span>
    </li>
    <li>
      <svg viewBox="0 0 16 16"><path d="M8 0a8 8 0 1 0 0 16A8 8 0 0 0 8 0zm0 2a6 6 0 0 1 5.7 4H10L8 4 6 6 4 5 2.4 6.5A6 6 0 0 1 8 2zm-5.8 6.5L5 9l1 3-1 1.2A6 6 0 0 1 2.2 8.5zM9 13.9V12l2-2 2.6.6A6 6 0 0 1 9 13.9z"/></svg>
      <span>www.hartiganelx.com.au</span>
    </li>
  </ul>
</section>

</body>
</html>
```